Wordpress Frontpage/Theme redesign with Female Touch

We’d like to get a new Wordpress theme or childtheme to refresh our beloved website: ladiesinventure.com.au which is a customized version of theme ‘Plume’ that we now find a bit “childish” “chaotic” “unprofessional looking”. We are after a more clear and refined, more professionally looking site.

We’d like to use our current plugins, somebody just needs to redesign the frontpage to give us a new and awesome outlook. We can install and finetune all the necessary plugins.
We know exactly what elements we want to see on the website, see detailed Design requirements. Please also feel free to use any images from http://ladiesinventure.com.au/category/Gallery/ or other stock images.

What we like:
We’d like to have a more professional look, we like ‘news sites’ that: feminine, intelligent, exclusive, smart, elegant, confident aiming towards the higher end of the female entrepreneur market. Websites like:
http://www.gildedhour.com/
http://www.velvira.com/velvira/
http://brightveil.quorvane.com.au/
http://pertlisbon.com/
http://skinmarket.example/item/pagelark-flat-journal-theme-/full_screen_preview/4719302

Reason: Hi guys, We are extending the deadline of the project as we are still waiting for the perfect design. Good luck everyone! Cheers

Target Market(s)

Australian national community of like-minded aspiring and accomplished female entrepreneurs. Age women in their 30’s and 40’s – typically confident and established powerful and driven, passionate women.

Requirements
Must have
• Detailed Design Requirements
• Read together with “Ladies in Venture website screenshot with numbers.jpg”:
• 1. Logo: New Logo provided + we need the tagline with nice characters
• 2. Social Media Buttons should be in the Footer: Chirrup, Faceplate, Tackboard, WorkLoop, Feed
• 3. Drop down Menu (Multi level) JOIN menu highlighted
• 4. Picture slideshow where we can put our photos, adds, event pictures, happy women faces etc.
• 5. Search with Search button
• 6. Space which is easy to edit and where we can quickly write news, or important information
• 7. Widget: News Letter Signup (Should be highlighted and well visible)
• 8. Widget: Login with standard Faceplate login button (Unipass plugin) this can be at top row header
• 9. Widget: Question of the week, Online poll
• 10. Widget: Upcoming events, Ticketeer widget
• 11. Featured Video Display: 2 videos which are in the “featured videos” category, (photo + excerpt)
• 12. Featured Blog Display: Displaying blog entries which are in the “featured blogs” category (photo + excerpt)
• 13. Widgets Standard Wordpress widgets to show recent activities (can be different)
• 14. Same as 13.
• 15. Same as 13.
• 16. Same as 13.
• 17. Faceplate News Feed
• 18. Footer: Social media buttons see no.2., + credit, etc..
• .
• + New features we need:
• 19. Featured members (displaying Level2 users from Q7 Roster Plugin)
• 20. Promo ClipTube Video: fix space on the top somewhere, picture provided.
• 21. Place for advertisements
• Other requirements:
• • Speed: Please don’t create huge background images/javascript files, current Frontpage is ~600KB.
• • Security: no hidden codes, no well known vulnerabilities.
• • Compatibility: please use standard Wordpress features. Later on we want to add more features like: Webshop, Pallounge
• • Resizable: When we change window size, or see it on mobile, it rearranges itself.

```html
<!DOCTYPE html>
<html lang="en">
<head>
<meta charset="utf-8">
<title>Ladies in Venture</title>
<link href="https://fonts.googleapis.com/css2?family=Open+Sans:wght@300;400;600;700&display=swap" rel="stylesheet">
<style>
:root{
  --pink:#e8087f;
  --pink-light:#f0479e;
  --orange:#f7941d;
  --orange-dark:#f07f12;
  --plum:#7a0e4a;
  --ink:#222;
  --text:#555;
  --muted:#888;
  --line:#e2e2e2;
  --panel-bg:#fff;
  --page-bg:#f6f6f6;
  --footer:#2b2b2b;
  --footer-deep:#1f1f1f;
  --fb-blue:#3b5998;
  --link-blue:#2a3f8f;
  --ad-red:#d3102c;
}
*{box-sizing:border-box;margin:0;padding:0}
html,body{width:1200px;height:2791px;overflow:hidden}
body{font-family:"Open Sans",Arial,sans-serif;color:var(--text);background:var(--page-bg);position:relative;font-size:13px}
.topline{position:absolute;top:0;left:0;width:1200px;height:6px;background:var(--pink)}
.header{position:absolute;top:6px;left:0;width:1200px;height:2455px;background:#fff}
.abs{position:absolute}

/* brand */
.brand{left:86px;top:46px;display:flex;align-items:center;gap:18px}
.brand-square{width:66px;height:66px;background:var(--pink);border-radius:6px}
.brand-name{font-size:40px;font-weight:300;color:var(--pink);letter-spacing:-.3px}
.search{left:845px;top:78px;width:268px;height:30px;border:1px solid #d6d6d6;display:flex}
.search span{flex:1;font-size:11px;font-style:italic;color:#999;padding:7px 10px}
.search .btn{width:38px;border-left:1px solid #d6d6d6;background:#f3f3f3;display:flex;align-items:center;justify-content:center}

/* nav */
.nav{left:84px;top:122px;width:1029px;height:53px;background:linear-gradient(#f21c93,#e0077b);display:flex}
.nav a{color:#fff;text-decoration:none;font-size:17px;font-weight:600;display:flex;align-items:center;padding:0 22px;border-right:1px solid rgba(255,255,255,.25)}
.nav .join{margin-left:auto;background:var(--plum);border:none;padding:0 40px 0 46px;clip-path:polygon(22px 0,100% 0,100% 100%,0 100%)}

/* slider */
.slider{left:84px;top:186px;width:724px;height:348px;background:linear-gradient(110deg,#5f6a7a 0%,#a4acb6 35%,#e9d9c6 60%,#f4efe9 100%)}
.slider-caption{position:absolute;left:0;bottom:0;width:100%;height:68px;background:rgba(255,255,255,.85);padding:10px 26px}
.slider-caption h2{font-size:21px;font-weight:400;color:var(--ink)}
.slider-caption p{font-size:11px;color:#666}
.slider-arrow{position:absolute;right:18px;bottom:14px;width:38px;height:38px;border-radius:50%;background:var(--pink)}

/* side panels */
.panel{background:var(--panel-bg);border:1px solid var(--line)}
.panel-title{font-size:19px;font-weight:400;color:#333;text-transform:uppercase;padding:16px 22px 12px;border-bottom:1px solid var(--line)}
.newsletter{left:817px;top:186px;width:297px;height:178px;background:linear-gradient(var(--orange),var(--orange-dark));padding:18px 26px;color:#fff}
.newsletter h3{font-size:20px;font-weight:600}
.newsletter p{font-size:11px;margin-bottom:10px}
.field{height:28px;background:rgba(255,255,255,.3);font-size:11px;padding:6px 12px;margin-bottom:8px;border-radius:2px;color:#fff}
.newsletter .signup{position:absolute;right:22px;bottom:16px;background:#8a4a0c;font-size:12px;font-weight:600;padding:5px 12px}
.login{left:817px;top:374px;width:297px;height:160px;padding:14px 26px}
.login h3{font-size:19px;font-weight:400;color:#333}
.login p{font-size:11px;color:#666;margin-bottom:12px}
.login .row{display:flex;gap:10px;margin-bottom:12px}
.login .row span{flex:1;height:24px;border:1px solid #ccc;font-size:11px;padding:3px 8px;color:#888}
.btn-pink{background:var(--pink);color:#fff;font-size:11px;font-weight:700;padding:5px 12px;display:inline-block;border-radius:2px}
.btn-fb{display:inline-block;background:var(--fb-blue);color:#fff;font-size:10px;padding:6px 14px;margin-left:12px;border-radius:3px}

.section-title{font-size:20px;font-weight:600;text-transform:uppercase;padding:20px 28px 10px}
.featured-video{left:84px;top:552px;width:724px;height:462px}
.featured-video .section-title{color:var(--pink)}
.video{display:flex;gap:18px;padding:8px 28px 10px}
.thumb{width:278px;height:178px;border:1px solid #ddd;padding:4px;flex-shrink:0}
.thumb div{width:100%;height:100%;position:relative}
.play{position:absolute;left:50%;top:50%;margin:-20px 0 0 -20px}
.video h4{font-size:21px;font-weight:400;color:var(--ink);line-height:1.3}
.video .sub{font-size:12px;color:#666;margin:4px 0 10px}
.byline{font-size:12px;color:var(--pink);margin-bottom:8px}
.video .ex{font-size:12px;line-height:1.6}

.question{left:817px;top:552px;width:297px;height:272px}
.question .panel-title{background:var(--pink);color:#fff;border:none}
.question .q{font-size:12px;color:#333;padding:12px 28px 8px}
.question li{list-style:none;font-size:12px;color:#666;padding:4px 28px 4px 46px;position:relative}
.question li::before{content:"";position:absolute;left:28px;top:8px;width:10px;height:10px;border:1px solid #bbb;border-radius:50%}
.question .btns{padding:12px 28px}
.btn-dark{display:inline-block;background:#222;color:#fff;font-size:11px;font-weight:700;padding:5px 12px;margin-left:6px;border-radius:2px}

.list li{list-style:none;font-size:12px;color:#666;padding:6px 0 5px 16px;margin:0 22px;border-bottom:1px solid #eee;position:relative}
.list li::before{content:"›";position:absolute;left:0;top:3px;font-size:15px;color:#999}
.recent{left:817px;top:837px;width:297px;height:310px}
.event{left:817px;top:1164px;width:297px;height:170px}
.event .body{display:flex;gap:14px;padding:12px 22px}
.event .img{width:92px;height:78px;background:linear-gradient(#b3778c,#7a5560);flex-shrink:0}
.event h5{font-size:13px;color:var(--orange);font-weight:600}
.event p{font-size:11px;color:#888;line-height:1.5}
.event .date{color:var(--orange)}
.categories{left:817px;top:1346px;width:297px;height:402px}
.archives{left:817px;top:1761px;width:297px;height:409px}

/* advert */
.ad{left:817px;top:2185px;width:297px;height:248px;background:#111;border:3px solid var(--ad-red);color:#fff;padding:18px 14px;overflow:hidden}
.ad .get{font-size:32px;font-weight:300;line-height:1.2}
.ad .only{font-size:20px;font-weight:300;margin-top:4px}
.ad .price{display:flex;align-items:flex-start;gap:6px;margin-top:-2px}
.ad .price .num{font-size:80px;font-weight:300;line-height:1}
.ad .price .per{font-size:17px;font-weight:300;line-height:1.15;margin-top:22px}
.ad .cover{position:absolute;right:10px;top:64px;width:118px;height:146px;background:linear-gradient(#e58ab4,#c24d7f)}
.ad .cta{position:absolute;left:14px;bottom:16px;background:var(--ad-red);font-size:12px;font-weight:700;padding:5px 12px}
.ad .ribbon{position:absolute;right:-40px;top:37px;width:170px;text-align:center;transform:rotate(45deg);background:var(--ad-red);font-size:9px;font-weight:700;padding:4px 0}

.articles{left:84px;top:1028px;width:724px;height:445px}
.articles .section-title{color:var(--orange)}
.article{display:flex;gap:18px;padding:14px 28px 14px;border-bottom:1px solid var(--line)}
.article:last-child{border:none}
.article .img{width:118px;height:88px;flex-shrink:0;background:linear-gradient(#8a6f66,#3e3030)}
.article h4{font-size:18px;font-weight:400;color:var(--ink);line-height:1.35;margin-bottom:4px}
.article p{font-size:12px;line-height:1.6}

.news{left:84px;top:1484px;width:724px;height:869px}
.news .section-title{color:#222}
.post{display:flex;gap:18px;padding:8px 28px 16px}
.avatar{width:84px;height:66px;border:1px solid #ddd;display:flex;align-items:center;justify-content:center;flex-shrink:0}
.avatar span{width:34px;height:34px;background:var(--pink);border-radius:4px}
.post h5{font-size:13px;color:var(--link-blue);font-weight:600;margin-bottom:2px}
.post p{font-size:11px;line-height:1.65;color:#555}
.fblike{display:inline-block;background:var(--fb-blue);color:#fff;font-size:10px;font-weight:700;padding:2px 8px;border-radius:2px;margin-top:4px}
.share{border:1px solid #ddd;background:#f7f7f7;padding:8px 10px;margin-top:10px;width:480px}
.share b{font-size:10px;color:var(--link-blue);display:block}
.share span{font-size:9px;color:#777;display:block}
.likes{padding:0 28px}
.likes p{font-size:11px;color:#333;margin-bottom:8px}
.likes p em{font-style:normal;color:var(--link-blue)}
.faces{width:660px;height:122px;background:linear-gradient(90deg,#9b8a80,#c7b2a6,#7f8ea0,#b89b8a,#a08a7e)}
.likes .plugin{font-size:10px;color:#555;border-top:1px solid #ddd;margin-top:14px;padding-top:8px}

.footer{position:absolute;left:0;top:2461px;width:1200px;height:251px;background:var(--footer);padding:40px 0 0 88px;display:flex;color:#ccc}
.footer h6{font-size:19px;font-weight:400;color:#fff;margin-bottom:12px}
.footer li{list-style:none;font-size:12px;padding:4px 0}
.footer .arrowed li::before{content:"›";margin-right:8px;color:#999}
.col1{width:178px}.col2{width:250px}.col3{width:262px}
.social{display:flex;gap:10px}
.social span{width:24px;height:24px;border-radius:3px;background:#6a6a6a}
.bottom{position:absolute;left:0;top:2712px;width:1200px;height:79px;background:var(--footer-deep);padding:30px 75px;font-size:12px;color:#888}
</style>
</head>
<body>
<div class="topline"></div>
<div class="header">
  <div class="abs brand"><span class="brand-square"></span><span class="brand-name">Ladies in Venture</span></div>
  <div class="abs search"><span>Search here..</span><div class="btn"><svg width="16" height="16" viewBox="0 0 16 16"><circle cx="6.5" cy="6.5" r="5" fill="none" stroke="#666" stroke-width="1.6"/><line x1="10.2" y1="10.2" x2="15" y2="15" stroke="#666" stroke-width="1.8"/></svg></div></div>

  <nav class="abs nav">
    <a>HOME</a><a>ABOUT US</a><a>RESOURCES</a><a>EVENTS</a><a>BIZ DIRECTORY</a><a>PARTNERS</a><a>CONTACT</a><a class="join">JOIN</a>
  </nav>

  <div class="abs slider" role="img" aria-label="Slideshow photo of a smiling businesswoman in front of blurred colleagues">
    <div class="slider-caption"><h2>Lorem ipsum dolor sit amet consectetuer</h2><p>Duis tincidunt lectus quis dui viverra vestibulum Suspendisse vulputate</p></div>
    <svg class="slider-arrow" viewBox="0 0 38 38"><circle cx="19" cy="19" r="19" fill="#e8087f"/><path d="M16 13l-6 6 6 6M22 13l6 6-6 6" fill="none" stroke="#fff" stroke-width="2"/></svg>
  </div>

  <div class="abs newsletter">
    <h3>SIGN UP NEWSLETTERS</h3>
    <p>Please subscriber here for latest news.</p>
    <div class="field">your name</div>
    <div class="field">email address</div>
    <span class="signup">SIGN UP</span>
  </div>

  <div class="abs panel login">
    <h3>MEMBER LOGIN</h3>
    <p>Please login here or connect with Faceplate</p>
    <div class="row"><span>username</span><span>password</span></div>
    <span class="btn-pink">LOGIN</span><span class="btn-fb">Connect with Faceplate</span>
  </div>

  <section class="abs panel featured-video">
    <h2 class="section-title">Featured Video</h2>
    <div class="video">
      <div class="thumb"><div role="img" aria-label="Video still: illustrated group of women icons" style="background:linear-gradient(135deg,#1e88d6,#6cc3f2)">
        <svg class="play" width="40" height="40" viewBox="0 0 40 40"><circle cx="20" cy="20" r="19" fill="rgba(0,0,0,.7)" stroke="#fff" stroke-width="2"/><path d="M16 12l12 8-12 8z" fill="#fff"/></svg></div></div>
      <div>
        <h4>Ladies in Venture<br>Testimonial Video</h4>
        <p class="sub">Ladies in Venture Testimonial Video</p>
        <p class="byline">Edda Morvane, March 6, 2013</p>
        <p class="ex">Ladies in Venture (LV), is the No.1. community for Australian female entrepreneurs, run by Edda Morvane and focuses on empowerment of women and equal opportunity advocacy.</p>
      </div>
    </div>
    <div class="video">
      <div class="thumb"><div role="img" aria-label="Video still: woman with glasses beside interview title" style="background:linear-gradient(90deg,#c9a98e,#e9e4dc 60%,#f4f4f4)">
        <svg class="play" width="40" height="40" viewBox="0 0 40 40"><circle cx="20" cy="20" r="19" fill="rgba(0,0,0,.7)" stroke="#fff" stroke-width="2"/><path d="M16 12l12 8-12 8z" fill="#fff"/></svg></div></div>
      <div>
        <h4>Melbourne Interviews<br>Part 3 3/3</h4>
        <p class="sub">Melbourne Interviews Part 3 3/3</p>
        <p class="byline">Edda Morvane, January 11, 2013</p>
        <p class="ex">This video is part 3 of a series of 3 videos discussing the advantages of being a woman in startup land, the importance of mentorship and helping other women in business.</p>
      </div>
    </div>
  </section>

  <aside class="abs panel question">
    <h3 class="panel-title">Question of the Week</h3>
    <p class="q">Are you Selling Overseas?</p>
    <ul>
      <li>Suspendisse vulputate aliquam dui.</li>
      <li>Nulla elementum dui ut augue.</li>
      <li>Aliquam vehicula mi at mauris.</li>
      <li>Maecenas placerat nisi at consequat rhoncus sem nunc gravida</li>
    </ul>
    <div class="btns"><span class="btn-pink">View Results</span><span class="btn-dark">Poll Achives</span></div>
  </aside>

  <aside class="abs panel recent">
    <h3 class="panel-title">Recent Posts</h3>
    <ul class="list">
      <li>Phasellus felis dolor scelerisque</li><li>A tempus eget lobortis id libero.</li><li>Donec scelerisque leo ac risus.</li><li>Praesent sit amet est.</li><li>In dictum dolor eu dictum porttitor</li><li>Enim felis viverra mi</li><li>Eget luctus massa purus quis odio.</li><li>Etiam nulla massa</li>
    </ul>
  </aside>

  <aside class="abs panel event">
    <h3 class="panel-title" style="border:none;padding-bottom:4px">Upcoming Event</h3>
    <div class="body">
      <div class="img" role="img" aria-label="Event photo of women at a gathering"></div>
      <div><h5>Morbi diam mauris</h5><p>Proin nulla arcu, non-ummy luctus, dictum eget, fermentum et, lorem</p><p class="date">November 28, 2013</p></div>
    </div>
  </aside>

  <aside class="abs panel categories">
    <h3 class="panel-title">Categories</h3>
    <ul class="list">
      <li>Articles</li><li>Empowerment of Women</li><li>Featured Articles</li><li>Featured Video</li><li>Female Empowerment</li><li>Gallery</li><li>Guest Blog</li><li>Interview</li><li>News</li><li>Video</li><li>Video Interview</li>
    </ul>
  </aside>

  <aside class="abs panel archives">
    <h3 class="panel-title">Archives</h3>
    <ul class="list">
      <li>November 2013</li><li>October 2013</li><li>September 2013</li><li>August 2013</li><li>July 2013</li><li>June 2013</li><li>May 2013</li><li>April 2013</li><li>March 2013</li><li>February 2013</li><li>January 2013</li>
    </ul>
  </aside>

  <aside class="abs ad">
    <div class="cover" role="img" aria-label="Magazine covers"></div>
    <div class="ribbon">LIMITED TIME OFFER</div>
    <div class="get">Get Velvira</div>
    <div class="only">Only</div>
    <div class="price"><span class="num">$1</span><span class="per">an<br>issue</span></div>
    <div class="cta">SUBSCRIBE NOW ›</div>
  </aside>

  <section class="abs panel articles">
    <h2 class="section-title">Featured Articles</h2>
    <article class="article"><div class="img" role="img" aria-label="Portrait photo for article"></div><div><h4>Cleansing the Workspace</h4><p>It is quite a common occurrence for me to go into people's business and find the energy and space quite chaotic.</p></div></article>
    <article class="article"><div class="img" role="img" aria-label="Portrait photo for article"></div><div><h4>Little Known Publicity Secret Revealed</h4><p>So often when people think of publicity and getting their names in the media, they think of national TV, major daily newspapers or high rating radio</p></div></article>
    <article class="article"><div class="img" role="img" aria-label="Photo of a group of entrepreneurs"></div><div><h4>Migrant entrepreneurs overcome barriers to starting up businesses in Australia</h4><p>Migrant entrepreneurs face an almighty battle when launching a start-up in Australia. They might have little money to start, and bank loans are nearly impossible to secure given the lack of recognised savings by our banks. Leases are also extremely hard to secure.</p></div></article>
  </section>

  <section class="abs panel news">
    <h2 class="section-title">News</h2>
    <div class="post"><div class="avatar"><span></span></div><div><h5>Ladies in Venture</h5><span class="fblike">Like</span></div></div>
    <div class="post"><div class="avatar"><span></span></div><div>
      <h5>Ladies in Venture</h5>
      <p>This happens when you get over your fear...WOW. http://hollowmere.com/nervous-man-nearly-in-tears-blows-the-star-trial-crowd-away/ #AnythingIsPossible Have an inspiring weekend folks!</p>
      <div class="share"><b>Nervous Man Nearly in Tears Blows The Star Trial Crowd Away</b><span>hollowmere.com</span><span>Video: Nervous Man Nearly in Tears Ends Up Blowing The Star Trial Crowd Away</span></div>
    </div></div>
    <div class="post"><div class="avatar"><span></span></div><div>
      <h5>Ladies in Venture</h5>
      <p>BOOST YOUR ONLINE PRESENCE THIS XMAS, so you won't be embarrassed to give away your business card at the Xmas parties ahead! Hello ladies! We have ONLY 1 spot available for the FIRST EVER OFFICIAL Ladies in Venture DIGITAL BRANDING MAKEOVER in Sydney, on Saturday, 14th December. We'll be doing a 'Behind the Scenes' video on the day to promote the program next year, so the women coming for this first session will gain a lot of additional EXPOSURE! What's included?</p>
      <p>- DIGITAL STRATEGY SESSION PRIOR PHOTO SHOOT</p>
      <p>- PROFESSIONAL HAIR/MAKE-UP, PHOTO SHOOT with one of the country's best brand photographer, 3 EDITED IMAGES to take home (additional images as incentives)</p>
      <p>- CONCEPT WORK, DESIGN - 5 SOCIAL MEDIA BRANDING IMAGES across these platforms: Faceplate background image, Chirrup, ClipTube, WorkLoop, Circlet</p>
      <p>- PROMOTION via the LV site &amp; our PR/Media channels</p>
      <p>The day will be fully catered, and will be gorgeous and exclusive with gift bags and lots of surprises Investment: $2,470 for non members, $1,970 for LV members. Fill out</p>
    </div></div>
    <div class="likes" style="margin-top:40px">
      <p>2,043 people like <em>Ladies in Venture</em>.</p>
      <div class="faces" role="img" aria-label="Grid of member profile photos"></div>
      <p class="plugin">Faceplate social plugin</p>
    </div>
  </section>
</div>

<footer class="footer">
  <div class="col1"><h6>Quick Links</h6><ul><li>Cum sociis</li><li>Natoque penatibus</li><li>Magnis dis parturient</li><li>Montes nascetur</li><li>Ridiculus mus</li></ul></div>
  <div class="col2"><h6>Recent Posts</h6><ul class="arrowed"><li>Diam mauris viverra in</li><li>Gravida mattis in ante.</li><li>Eget arcu Morbi porta</li><li>Ullamcorper nonummy</li></ul></div>
  <div class="col3"><h6>News Features</h6><ul class="arrowed"><li>Morbi diam mauris viverra in</li><li>Gravida mattis in ante.</li><li>Morbi eget arcu Morbi porta</li><li>Libero id ullamcorper nonummy</li></ul></div>
  <div><h6>Get Connected</h6><div class="social"><span aria-label="Faceplate"></span><span aria-label="Chirrup"></span><span aria-label="WorkLoop"></span><span aria-label="Feed"></span><span aria-label="Tackboard"></span></div></div>
</footer>
<div class="bottom">© 2013 Company Name.  All right reserved.  Term of Use</div>
</body>
</html>
```